Poster to display corporate values and behaviors associated

I'm looking for a graphic design, probably in the form of a poster or something that can be posted on walls throughout the building that identifies our "Brightwell Values".
The values are: Accountability, Honesty, Excellence, Teamwork, and Family.
Associated behaviors (which I'd like displayed with each value) are:
Accountability: Integrity, Trust, Self-Discipline, Tranparency
Honesty: Integrity, Pschological Safety, Vulnerability, Dependable, Ethical, Truthful
Excellence: Consistent Quality, Continuous Improvement, Attention to Detail, Accepting Challenges, Service to others (internally and externally)
Teamwork: Acknowledging strengths and weaknesses, Compromise, Active listening, Punctuality, Open to Feedback, Mutual Respect
Family: Acceptance, Compassion, Being there for each other, Celebrating Successes
I have attached an example that my team put together, however it is too small for something on the wall, and am looking for other options.
Feel free to use our corporate logo as well (attached)

```html
<!DOCTYPE html>
<html lang="en">
<head>
<meta charset="utf-8">
<title>Brightwell Values</title>
<link href="https://fonts.googleapis.com/css2?family=Montserrat:wght@300;400;500;700&display=swap" rel="stylesheet">
<style>
  :root {
    --bg: #ffffff;
    --ink: #333333;
    --disc: #e6e6e6;
    --teamwork: #b65cf5;
    --excellence: #f0605a;
    --family: #2ebfa5;
    --honesty: #1a6ef0;
    --accountability: #f7a928;
  }
  html, body {
    margin: 0;
    padding: 0;
    overflow: hidden;
    background: var(--bg);
  }
  .poster {
    position: relative;
    width: 1200px;
    height: 675px;
    overflow: hidden;
    background: var(--bg);
    font-family: "Montserrat", sans-serif;
    color: var(--ink);
  }
  .flower {
    position: absolute;
    left: 0;
    top: 0;
    width: 1200px;
    height: 675px;
  }
  .value {
    position: absolute;
  }
  .value--right { text-align: right; }
  .value--left { text-align: left; }
  .value__title {
    margin: 0 0 10px;
    font-size: 18px;
    font-weight: 500;
    line-height: 1.2;
  }
  .value__behaviours {
    margin: 0;
    font-size: 12.2px;
    font-weight: 300;
    line-height: 18.3px;
  }
  .value--teamwork { right: 731px; top: 88px; width: 215px; }
  .value--teamwork .value__title { color: var(--teamwork); }
  .value--family { right: 917px; top: 278px; width: 185px; }
  .value--family .value__title { color: var(--family); }
  .value--honesty { right: 847px; top: 485px; width: 190px; }
  .value--honesty .value__title { color: var(--honesty); }
  .value--excellence { left: 916px; top: 252px; width: 220px; }
  .value--excellence .value__title { color: var(--excellence); }
  .value--accountability { left: 861px; top: 475px; width: 150px; }
  .value--accountability .value__title { color: var(--accountability); }
  .hub-label {
    font-family: "Montserrat", sans-serif;
    font-weight: 700;
    font-size: 22px;
    fill: #111111;
  }
</style>
</head>
<body>
<main class="poster">
  <svg class="flower" viewBox="0 0 1280 720" aria-hidden="false">
    <defs>
      <path id="petal-near" d="M -26 -60 C -45 -100, -73 -135, -73 -175 A 73 73 0 1 1 73 -175 C 73 -135, 45 -100, 26 -60 Z"/>
      <path id="petal-mid" d="M -30 -60 C -50 -110, -73 -155, -73 -202 A 73 73 0 1 1 73 -202 C 73 -155, 50 -110, 30 -60 Z"/>
      <path id="petal-far" d="M -30 -60 C -52 -120, -73 -175, -73 -224 A 73 73 0 1 1 73 -224 C 73 -175, 52 -120, 30 -60 Z"/>
      <linearGradient id="grad-teamwork" x1="0" y1="0" x2="1" y2="1"><stop offset="0" stop-color="#c878fa"/><stop offset="1" stop-color="#8614f0"/></linearGradient>
      <linearGradient id="grad-excellence" x1="0" y1="0" x2="1" y2="1"><stop offset="0" stop-color="#f57a72"/><stop offset="1" stop-color="#e61616"/></linearGradient>
      <linearGradient id="grad-family" x1="0" y1="0" x2="1" y2="1"><stop offset="0" stop-color="#3dc9b0"/><stop offset="1" stop-color="#1e9485"/></linearGradient>
      <linearGradient id="grad-honesty" x1="0" y1="0" x2="1" y2="1"><stop offset="0" stop-color="#2a7cf5"/><stop offset="1" stop-color="#0848bd"/></linearGradient>
      <linearGradient id="grad-accountability" x1="0" y1="0" x2="1" y2="1"><stop offset="0" stop-color="#fbb940"/><stop offset="1" stop-color="#ec9506"/></linearGradient>
      <radialGradient id="grad-disc" cx="0.4" cy="0.35" r="0.7"><stop offset="0" stop-color="#ececec"/><stop offset="1" stop-color="#dcdcdc"/></radialGradient>
      <filter id="soft-shadow" x="-30%" y="-30%" width="160%" height="160%">
        <feDropShadow dx="0" dy="4" stdDeviation="5" flood-color="#000" flood-opacity="0.28"/>
      </filter>
      <filter id="petal-glow" x="-30%" y="-30%" width="160%" height="160%">
        <feDropShadow dx="0" dy="2" stdDeviation="6" flood-color="#000" flood-opacity="0.15"/>
      </filter>
    </defs>

    <g class="petals" transform="translate(640 360)" filter="url(#petal-glow)">
      <use href="#petal-near" fill="url(#grad-teamwork)"/>
      <use href="#petal-mid" fill="url(#grad-excellence)" transform="rotate(77)"/>
      <use href="#petal-mid" fill="url(#grad-family)" transform="rotate(-77)"/>
      <use href="#petal-far" fill="url(#grad-accountability)" transform="rotate(147)"/>
      <use href="#petal-far" fill="url(#grad-honesty)" transform="rotate(-147)"/>
    </g>

    <g class="discs" fill="url(#grad-disc)" filter="url(#soft-shadow)">
      <circle cx="640" cy="185" r="55"/>
      <circle cx="837" cy="315" r="55"/>
      <circle cx="442" cy="315" r="55"/>
      <circle cx="518" cy="548" r="55"/>
      <circle cx="763" cy="548" r="55"/>
      <circle cx="640" cy="360" r="93"/>
    </g>

    <!-- teamwork icon: group of people -->
    <g class="icon icon--teamwork" fill="var(--teamwork)">
      <circle cx="640" cy="160" r="6"/>
      <rect x="632" y="168" width="16" height="20" rx="4"/>
      <rect x="635" y="184" width="10" height="10" rx="2"/>
      <circle cx="624" cy="156" r="5"/>
      <rect x="617" y="163" width="13" height="18" rx="3"/>
      <circle cx="656" cy="156" r="5"/>
      <rect x="650" y="163" width="13" height="18" rx="3"/>
    </g>

    <!-- excellence icon: award rosette -->
    <g class="icon icon--excellence" fill="var(--excellence)">
      <path d="M 826 318 L 820 338 L 828 334 L 832 341 L 836 322 Z"/>
      <path d="M 848 318 L 854 338 L 846 334 L 842 341 L 838 322 Z"/>
      <circle cx="837" cy="306" r="15"/>
      <circle cx="837" cy="306" r="9" fill="var(--disc)"/>
      <circle cx="837" cy="306" r="5"/>
    </g>

    <!-- family icon: people in a heart -->
    <g class="icon icon--family" fill="var(--family)">
      <path d="M 442 335 C 420 320, 424 298, 438 302 L 442 306 L 446 302 C 460 298, 464 320, 442 335 Z"/>
      <circle cx="432" cy="296" r="5"/>
      <circle cx="452" cy="296" r="5"/>
      <circle cx="442" cy="318" r="5" fill="var(--disc)"/>
      <circle cx="442" cy="318" r="3"/>
    </g>

    <!-- honesty icon: handshake -->
    <g class="icon icon--honesty" fill="none" stroke="var(--honesty)" stroke-width="3.5" stroke-linejoin="round" stroke-linecap="round">
      <path d="M 501 542 L 509 536 L 520 538 L 530 536 L 536 542"/>
      <path d="M 505 548 L 514 557 Q 518 560 522 557 L 531 548"/>
      <path d="M 515 543 L 524 552"/>
    </g>

    <!-- accountability icon: person beside a checklist -->
    <g class="icon icon--accountability" fill="var(--accountability)">
      <circle cx="751" cy="538" r="4"/>
      <rect x="745" y="543" width="11" height="12" rx="2"/>
      <rect x="747" y="554" width="3" height="8"/>
      <rect x="752" y="554" width="3" height="8"/>
      <circle cx="770" cy="534" r="7" fill="none" stroke="var(--accountability)" stroke-width="2"/>
      <path d="M 766 534 L 769 537 L 774 531" fill="none" stroke="var(--accountability)" stroke-width="2"/>
      <rect x="760" y="545" width="4" height="3"/>
      <rect x="766" y="545" width="9" height="3"/>
      <rect x="760" y="551" width="4" height="3"/>
      <rect x="766" y="551" width="9" height="3"/>
      <rect x="760" y="557" width="4" height="3"/>
      <rect x="766" y="557" width="9" height="3"/>
    </g>

    <text class="hub-label" x="640" y="354" text-anchor="middle">BRIGHTWELL</text>
    <text class="hub-label" x="640" y="382" text-anchor="middle">VALUES</text>
  </svg>

  <section class="value value--right value--teamwork">
    <h2 class="value__title">Teamwork</h2>
    <p class="value__behaviours">Acknowledging strengths and weaknesses, Compromise, Active listening, Punctuality, Open to Feedback, Mutual Respect</p>
  </section>

  <section class="value value--right value--family">
    <h2 class="value__title">Family</h2>
    <p class="value__behaviours">Acceptance, Compassion, Being there for each other, Celebrating Successes</p>
  </section>

  <section class="value value--right value--honesty">
    <h2 class="value__title">Honesty</h2>
    <p class="value__behaviours">Integrity, Pschological Safety, Vulnerability, Dependable, Ethical, Truthful</p>
  </section>

  <section class="value value--left value--excellence">
    <h2 class="value__title">Excellence</h2>
    <p class="value__behaviours">Consistent Quality, Continuous Improvement, Attention to Detail, Accepting Challenges, Service to others (internally and externally)</p>
  </section>

  <section class="value value--left value--accountability">
    <h2 class="value__title">Accountability</h2>
    <p class="value__behaviours">Integrity, Trust, Self-Discipline, Tranparency</p>
  </section>
</main>
</body>
</html>
```